Lani Wellness Clinic Website - this is a website for a medical practice

This is a medical practice and would like my logo to be presented. I have attached a copy of some copy that should give you an idea of what my practice is about. My practice will be seeing Elderaid patients in their homes. No coming to the office for a visit. I listen to my patients and provide individualized care. The name "Lani" means star in Hawaiʻian and want the patient to feel that they are the main focus of my practice.

Target Market(s)

Elderaid patients

Industry/Entity Type

medical

Coding

Coded - Design and coding required

Number of Pages Required

2 page

Font styles to use
Sans Serif

Colors
00AB8E
00BBA5
67D7C9
C6EFE9
E9F9F6

Requirements
Must have
• feeling that I care about each patient and that I will do my very best to keep them as healthy as possible, that the Hawaiʻian culture is represented. Simple and easy to navigate for someone who isnʻt tech savvy. In normal conversational language.
Nice to have
• The elderly in Hawaiʻi are called Kapuna and they are revered. I would like to convey that.
Should not have
• Medical jargon

```html
<!DOCTYPE html>
<html lang="en">
<head>
<meta charset="UTF-8">
<title>Lani Wellness Clinic</title>
<link href="https://fonts.googleapis.com/css2?family=Lato:wght@400;700&family=Montserrat:wght@400&display=swap" rel="stylesheet">
<style>
  :root{
    --green-deep:#00AB8E;
    --green:#00BBA5;
    --green-soft:#67D7C9;
    --green-pale:#C6EFE9;
    --green-mist:#E9F9F6;
    --text:#555a5c;
    --muted:#8c9092;
    --rule:#d9dcdc;
  }
  *{box-sizing:border-box;margin:0;padding:0}
  html,body{width:1200px;height:984px;overflow:hidden}
  body{
    font-family:"Lato",sans-serif;color:var(--text);
    background:linear-gradient(to bottom,#ececec 0,#f7f7f7 260px,#ffffff 520px);
    position:relative;
  }
  .page{position:absolute;left:145px;top:0;width:918px;height:984px;background:#fff}
  .announce{
    height:49px;background:var(--green-pale);color:var(--green-deep);
    font-weight:700;font-size:20px;display:flex;align-items:center;justify-content:center;
  }
  .site-header{height:94px;display:flex;align-items:center;justify-content:space-between;padding:0 30px 0 25px}
  .brand{font-family:"Montserrat",sans-serif;font-weight:400;font-size:34px;color:var(--green-deep);letter-spacing:.3px;text-transform:uppercase}
  .nav{display:flex;align-items:center;gap:38px}
  .nav a{text-decoration:none;font-weight:700;font-size:18px;text-transform:uppercase}
  .nav .home{color:var(--muted)}
  .nav .cta{background:var(--green);color:#fff;padding:0 28px;height:48px;display:flex;align-items:center;border-radius:3px}
  .hero{
    position:absolute;left:0;top:143px;width:918px;height:712px;
    background:
      radial-gradient(ellipse 260px 180px at 340px 300px,rgba(170,240,215,.85),transparent 70%),
      radial-gradient(ellipse 420px 260px at 918px 0,rgba(40,90,75,.9),transparent 75%),
      linear-gradient(to bottom,#5bb89f 0,#79cbb3 180px,#a8ddcc 330px,#e6f5f0 470px,#ffffff 600px);
  }
  .tagline{position:absolute;left:27px;top:125px;font-family:"Montserrat",sans-serif;color:#fff;text-transform:uppercase;line-height:1.25}
  .tagline .small{font-size:22px;display:block}
  .tagline .big{font-size:35px;display:block;margin:2px 0}
  .collage .shot{position:absolute;border:3px solid #fff;}
  .intro{
    position:absolute;left:28px;top:304px;width:862px;height:408px;
    background:linear-gradient(to bottom,rgba(255,255,255,.92),rgba(255,255,255,.97));
    padding:52px 30px 0 29px;display:flex;justify-content:space-between;
  }
  .intro-copy{width:560px}
  .intro-copy h1{font-size:20px;line-height:28px;font-weight:700;color:var(--green-deep);margin-bottom:24px}
  .intro-copy p{font-size:14.6px;line-height:22.5px;margin-bottom:22.5px}
  .intro-copy .link{color:var(--green-deep);font-weight:700;text-decoration:none}
  .director{width:217px;text-align:center;margin-top:3px}
  .director .portrait{width:217px;height:256px;background:linear-gradient(160deg,#b3c9c3,#a2b7b1 60%,#8a6f63);}
  .director .name{font-size:17.5px;font-weight:700;color:var(--green-deep);margin-top:16px}
  .director .role{font-size:15px;color:var(--muted);margin-top:3px}
  .site-footer{position:absolute;left:20px;top:893px;width:880px;border-top:1px solid var(--rule);text-align:center;padding-top:35px;font-size:15px}
</style>
</head>
<body>
<div class="page">
  <div class="announce">Telehealth Appointments Are Available!</div>
  <header class="site-header">
    <div class="brand">Lani Wellness Clinic</div>
    <nav class="nav">
      <a class="home" href="#">Home</a>
      <a class="cta" href="#">Contact Us</a>
    </nav>
  </header>

  <section class="hero">
    <div class="tagline">
      <span class="small">Providing</span>
      <span class="big">Quality Care</span>
      <span class="small">Since 2000</span>
    </div>

    <div class="intro">
      <div class="intro-copy">
        <h1>Lani means "star" in Hawai'ian and we want our patients to feel that they are the focus in our practice.</h1>
        <p>Lani Wellness Clinic is a leading medical clinic on O'ahu, dedicated to providing exceptional healthcare services to our patients. With a highly skilled and experienced Nurse Practitioner, we are committed to delivering personalized care.</p>
        <p>Our mission is to ensure the well-being of our patients by offering comprehensive medical services, including primary care, and preventive care.</p>
        <p>We prioritize patient comfort and convenience by visiting you in your home removing the need to drive to an office thereby minimizing wait times. On-call providers and same-day appointments whenever possible are offered.</p>
        <p><a class="link" href="#">CONTACT US TODAY</a> to experience the highest standard of healthcare.</p>
      </div>
      <div class="director">
        <div class="portrait" role="img" aria-label="Portrait photo of the clinic director"></div>
        <div class="name">Your Name Here</div>
        <div class="role">Director</div>
      </div>
    </div>

    <div class="collage">
      <div class="shot" style="left:306px;top:93px;width:128px;height:139px;background:linear-gradient(160deg,#6e8fa6,#b59a82 60%,#c9b79a)" role="img" aria-label="Photo of a smiling older woman holding a cup"></div>
      <div class="shot" style="left:412px;top:38px;width:148px;height:143px;background:linear-gradient(160deg,#8a7a6c,#c6a896 50%,#a58b7a)" role="img" aria-label="Close-up photo of a smiling elderly woman"></div>
      <div class="shot" style="left:631px;top:46px;width:171px;height:114px;background:linear-gradient(160deg,#c9a46a,#8a5f4a 50%,#c7b3a8)" role="img" aria-label="Photo of a smiling older couple"></div>
      <div class="shot" style="left:748px;top:112px;width:142px;height:152px;background:linear-gradient(160deg,#8f8a86,#a88d7b 50%,#d2ccc6)" role="img" aria-label="Photo of a smiling elderly woman with grey hair"></div>
      <div class="shot" style="left:449px;top:195px;width:140px;height:138px;background:linear-gradient(160deg,#6b5d4f,#c9a88f 50%,#d8d2cc)" role="img" aria-label="Photo of an older man holding an autumn leaf"></div>
      <div class="shot" style="left:619px;top:206px;width:171px;height:113px;background:linear-gradient(160deg,#b7a99c,#e0d2c6 50%,#cfc6be)" role="img" aria-label="Photo of two smiling elderly women"></div>
      <div class="shot" style="left:527px;top:125px;width:183px;height:107px;background:linear-gradient(160deg,#c6bfae,#a87e64 50%,#d8c27a)" role="img" aria-label="Photo of an older couple smiling together"></div>
    </div>
  </section>

  <footer class="site-footer">© 2024 Lani Wellness Clinic. All rights reserved.</footer>
</div>
</body>
</html>
```